Building company needs a letterhead design

I'm after a modern but professional letter head.
Must have the below details:
- Logo
- Website - TARVELGROUP.COM.AU
- Email - INFO@TARVELGROUP.COM.AU
- Office - 03 58206317
- Mobile number - 0413865290
- ABN - 47 318 264 105
...........................................................................................................................................................................................................................
- Logo
- Office - 03 58206317
- ABN - 47 318 264 105

Target Market(s)

.

Industry/Entity Type

Construction Company

Font styles to use
Sans Serif

Requirements
Must have
• Must have the below details:
• - Logo
• - Website - TARVELGROUP.COM.AU
• - Email - INFO@TARVELGROUP.COM.AU
• - Office - 03 58206317
• - Mobile number - 0413865290
• - ABN - 47 318 264 105
Nice to have
• .
Should not have
• .

```html
<!DOCTYPE html>
<html lang="en">
<head>
<meta charset="utf-8">
<title>Tarvel Building Group Letterhead</title>
<link rel="stylesheet" href="https://fonts.googleapis.com/css2?family=Arimo:wght@400;700&display=swap">
<style>
  :root {
    --bg: #e9e9e9;
    --paper: #ffffff;
    --charcoal: #2a2a2a;
    --charcoal-light: #3a3a3a;
    --gold: #f2b227;
    --gold-deep: #e29c12;
    --ink: #1e1e1e;
    --header-text: #f1f1f1;
    --swoosh: #ececec;
    --swoosh-line: #d6d6d6;
  }
  * { box-sizing: border-box; margin: 0; padding: 0; }
  html, body { width: 1200px; height: 720px; overflow: hidden; }
  body {
    background: var(--bg);
    font-family: "Arimo", Arial, sans-serif;
    color: var(--ink);
    position: relative;
  }
  .letterhead {
    position: absolute;
    left: 360px; top: 20px;
    width: 480px; height: 680px;
    background: var(--paper);
    box-shadow: 0 6px 24px rgba(0,0,0,.18);
    overflow: hidden;
  }
  .header {
    position: relative;
    height: 58px;
    background: linear-gradient(180deg, var(--charcoal-light), var(--charcoal));
    display: flex; justify-content: space-between; align-items: center;
    padding: 0 22px;
  }
  .brand { display: flex; align-items: center; gap: 8px; }
  .brand-square { width: 14px; height: 14px; background: var(--gold); flex: none; }
  .brand-name {
    color: var(--header-text);
    font-weight: 400;
    font-size: 13px;
    line-height: 1;
  }
  .header-info { text-align: right; font-size: 7px; line-height: 1.35; color: var(--header-text); letter-spacing: .3px; }
  .header-info .accent { color: var(--gold); }
  .swoosh { display: block; width: 100%; height: 60px; }
  .recipient {
    position: absolute; right: 26px; top: 100px;
    text-align: right; font-size: 7.5px; line-height: 1.38;
    font-style: normal; color: var(--ink);
  }
  .content {
    position: absolute; left: 30px; right: 26px; top: 180px;
    font-size: 8.2px; line-height: 1.42; color: var(--ink);
  }
  .content p { margin-bottom: 14px; }
  .sender { font-size: 9px; line-height: 1.3; margin-top: 10px; }
  .sender .credential { font-size: 6px; letter-spacing: .3px; }
  .signature { width: 90px; height: 34px; margin-top: 16px; background: linear-gradient(90deg, #f3f3f3, #e4e4e4); }
  .footer-mark {
    position: absolute; left: 50%; bottom: 52px; transform: translateX(-50%);
    width: 18px; height: 18px; background: var(--gold);
  }
  .footer {
    position: absolute; left: 0; right: 0; bottom: 0; height: 40px;
    background: linear-gradient(180deg, var(--gold), var(--gold-deep));
    display: flex; align-items: center; justify-content: center;
    font-size: 6.8px; font-weight: 700; color: var(--charcoal); letter-spacing: .3px;
  }
  .footer::before {
    content: ""; position: absolute; left: 0; right: 0; top: -4px; height: 2px; background: var(--gold);
  }
  .footer .sep { margin: 0 4px; }
</style>
</head>
<body>
  <main class="letterhead">
    <header class="header">
      <div class="brand">
        <span class="brand-square"></span>
        <span class="brand-name">Tarvel Building Group</span>
      </div>
      <div class="header-info">
        <div class="accent">WWW.TARVELGROUP.COM.AU</div>
        <div>REGISTERED BUILDING PRACTITIONER</div>
        <div class="accent">ABN: 47 318 264 105</div>
      </div>
    </header>
    <svg class="swoosh" viewBox="0 0 480 60" preserveAspectRatio="none" aria-hidden="true">
      <path d="M0 0 H480 V20 C360 10 200 55 0 50 Z" fill="var(--swoosh)"/>
      <path d="M0 38 C180 44 330 8 480 14" fill="none" stroke="var(--swoosh-line)" stroke-width="1.5"/>
      <path d="M0 46 C200 50 340 18 480 26" fill="none" stroke="#fff" stroke-width="2"/>
    </svg>

    <address class="recipient">
      Name of Recipient<br>Company Name<br>Address as required<br>City, Province<br>Country, Postal Code
    </address>

    <section class="content">
      <p>Salutation:</p>
      <p>Lorem ipsum dolor sit amet, consectetur adipiscing elit, sed diam nonumy eiusmod tempor incidunt ut labore et dolore magna aliquam erat volupat. Ut enim ad minimim veniami quis nostrud exercitation ullamcorper suscipit laboris nisi ut aliquip ex ea commodo consequat. Duis autem vel eum irure dolor in reprehenderit in voluptate velit esse molestaie son consequat, vel illum dolore eu fugiat nulla pariatur.</p>
      <p>At vero eos et accusam et justo odio dignissim qui blandit praesent lupatum delenit aigue duos dolor et molestais exceptur sint occaecat cupidat non provident, simil tempor sunt in culpa qui officia deserunt mollit anim id est dolor fugai. Et harum dereud facilis est er expedit distinct. Nam liber a tempor cum soluta nobis eligent optio comque nihil quod a impedit anim id quod maxim placeat facer possim omnis es voluptas assumenda est, omnis dolor repellend.</p>
      <p>Lorem ipsum dolor sit amet, consectetur adipiscing elit, sed diam nonumy eiusmod tempor incidunt ut labore et dolore magna aliquam erat volupat. Ut enim ad minimim veniami quis nostrud exercitation ullamcorper suscipit laboris nisi ut aliquip ex ea commodo consequat. Duis autem vel eum irure dolor in reprehenderit in voluptate velit esse molestaie son consequat, vel illum dolore.</p>
      <p>Complimentary closing</p>
      <div class="sender">
        Sender's Name, <span class="credential">CREDENTIAL</span><br>
        Title<br>
        Tel: 604-555-0182<br>
        Fax: 604-555-0182
      </div>
      <div class="signature" role="img" aria-label="Handwritten signature of the sender"></div>
    </section>

    <span class="footer-mark"></span>
    <footer class="footer">
      OFFICE PHONE: 03 58206317<span class="sep">|</span>MOBILE NUMBER: 0413865290<span class="sep">|</span>EMAIL: INFO@TARVELGROUP.COM.AU
    </footer>
  </main>
</body>
</html>
```